I need a feather flag designed for my business which states " HELICOPTER RIDES" and possibly adding my logo to them. This will be used for my helicopter ride business and we can put these up to show people where the rides will be .

Industry/Entity Type

aviation

Colors
00AB8E
00BBA5
67D7C9
C6EFE9
E9F9F6
EB3D1F
EC4F4E
F09395
F8D3D4
FCEDEE

Requirements
Must have
• logo

```html
<!DOCTYPE html>
<html lang="en">
<head>
<meta charset="utf-8">
<title>Skyvale Helicopters – Feather Flag</title>
<link href="https://fonts.googleapis.com/css2?family=Oswald:wght@500;700&display=swap" rel="stylesheet">
<style>
  :root {
    --page-bg: #e9ecec;
    --flag-teal: #2aab95;
    --flag-teal-light: #3bbca6;
    --flag-teal-dark: #22998a;
    --headline: #f4f6f6;
    --brand-ink: #33393b;
  }
  html, body {
    margin: 0;
    padding: 0;
    width: 1200px;
    height: 920px;
    overflow: hidden;
    background: var(--page-bg);
  }
  .canvas {
    width: 1200px;
    height: 920px;
    display: block;
  }
  .flag-body { fill: var(--flag-teal); }
  .flag-headline {
    font-family: "Oswald", sans-serif;
    font-weight: 700;
    fill: var(--headline);
  }
  .brand-name {
    font-family: "Oswald", sans-serif;
    font-weight: 700;
    fill: var(--brand-ink);
  }
  .brand-sub {
    font-family: "Oswald", sans-serif;
    font-weight: 700;
    fill: var(--brand-ink);
  }
</style>
</head>
<body>
<svg class="canvas" viewBox="0 0 1200 920" xmlns="http://www.w3.org/2000/svg">
  <defs>
    <clipPath id="feather-shape">
      <path d="M450,880 L450,150 Q450,40 570,42 Q700,46 750,92 L750,760 Q750,880 630,880 Z"/>
    </clipPath>
    <linearGradient id="pattern-tone" x1="0" y1="1" x2="1" y2="0">
      <stop offset="0" stop-color="var(--flag-teal-dark)"/>
      <stop offset="0.5" stop-color="var(--flag-teal)"/>
      <stop offset="1" stop-color="var(--flag-teal-light)"/>
    </linearGradient>
  </defs>

  <g class="feather-flag">
    <path class="flag-body" d="M450,880 L450,150 Q450,40 570,42 Q700,46 750,92 L750,760 Q750,880 630,880 Z"/>
    <rect class="flag-pattern" x="450" y="40" width="300" height="840"
          fill="url(#pattern-tone)" clip-path="url(#feather-shape)"
          role="img" aria-label="Faint swoosh and dot background pattern in teal tones"/>

    <g class="brand-lockup">
      <text class="brand-name" transform="translate(604,540) rotate(-90)" font-size="66" letter-spacing="1">SKYVALE</text>
      <text class="brand-sub" transform="translate(628,540) rotate(-90)" font-size="19" letter-spacing="9.5">HELICOPTERS</text>
    </g>

    <text class="flag-headline" transform="translate(712,830) rotate(-90)" font-size="86" textLength="720" lengthAdjust="spacingAndGlyphs">HELICOPTER RIDES</text>
  </g>
</svg>
</body>
</html>
```